VELMIRA (coffee package design)

Make coffee bag for coffee beans: VELMIRA is a quality-driven coffee roaster focused on crafting fresh, flavorful coffee from premium beans sourced directly from farms. We build close relationships with growers to ensure ethical practices, traceability, and exceptional quality at the origin. Our small-batch roasting approach brings out the unique character of each bean—highlighting bold notes, rich complexity, and peak freshness. At VELMIRA, we believe great coffee starts at the source—and ends in your cup, roasted to perfection.

**VELMIRA** is a quality-driven coffee roaster focused on crafting fresh, flavorful coffee from **premium beans sourced directly from farms**. We build close relationships with growers to ensure ethical practices, traceability, and exceptional quality at the origin. Our small-batch roasting approach brings out the unique character of each bean—highlighting bold notes, rich complexity, and peak freshness. At **VELMIRA**, we believe great coffee starts at the source—and ends in your cup, roasted to perfection.

VELMIRA

ETHICALLY SOURCED COFFEE

On Top: 100% Arabica Beans

On Left Side:
Coffee brew guide: https://in.snapfolio.net/pin/418273905561720394/
https://in.snapfolio.net/pin/coffee-brewing-method-chart--847215930466102/

On right side bottom:
STORAGE
Proper storage is essential to maintaining your coffee’s freshness and flavor. Once opened, we recommend keeping your coffee in a cool, dark, dry place and sealed in an airtight container. Always reseal the bag after each use to preserve maximum freshness and aroma.

482 Fenwick Oakland Ca 94613

Follow Us
www.velmira.com
TikTok@velmira
IG@tryvelmira

Target Market(s)

Coffee/ Cafe

Industry/Entity Type

Coffee

Font styles to use
Other font styles liked:
• Non‑Seasonal Sans

Requirements
Must have
• Clean, modern
Nice to have
• Elegant

```html
<!DOCTYPE html>
<html lang="en">
<head>
<meta charset="utf-8">
<title>VELMIRA – Coffee Bag Labels</title>
<link href="https://fonts.googleapis.com/css2?family=Barlow+Condensed:ital,wght@0,400;0,500;0,600;0,700;1,400;1,600&display=swap" rel="stylesheet">
<style>
  :root{
    --bg:#ececec;
    --navy:#1c3560;
    --navy-soft:#2a4677;
    --gold:#c49a3c;
    --gold-light:#e0bd63;
    --cream:#f4f3ec;
    --ink:#1c3560;
    --white:#ffffff;
  }
  *{box-sizing:border-box;margin:0;padding:0}
  html,body{width:1200px;height:1200px;overflow:hidden;background:var(--bg)}
  body{font-family:"Barlow Condensed",sans-serif;color:var(--ink);position:relative}

  .label{position:absolute;top:226px;width:520px;height:748px;border-radius:8px;overflow:hidden;background:var(--cream);box-shadow:0 2px 10px rgba(0,0,0,.06)}
  .label--back{left:60px}
  .label--front{left:620px}

  .label__pattern{position:absolute;left:0;top:0;width:100%;height:350px;
    background:linear-gradient(160deg,var(--navy-soft) 0%,var(--navy) 60%,#172c51 100%)}
  .label__band{position:absolute;left:0;top:350px;width:100%;height:9px;
    background:linear-gradient(90deg,var(--gold),var(--gold-light) 50%,var(--gold))}
  .seal{position:absolute;top:314px;left:50%;width:80px;height:80px;margin-left:-40px;border-radius:50%;
    background:radial-gradient(circle at 40% 35%,var(--gold-light),var(--gold) 70%);box-shadow:0 1px 3px rgba(0,0,0,.25)}

  .story{position:absolute;left:40px;right:40px;top:168px;text-align:center;color:var(--white);font-size:12.5px;line-height:1.55}
  .story strong{font-weight:700}

  .side-note{position:absolute;top:500px;right:-22px;width:140px;transform:translateY(-50%) rotate(-90deg);transform-origin:center;
    font-weight:700;font-size:15px;letter-spacing:.5px;color:var(--ink);white-space:nowrap;text-align:center}

  .brew-guide{position:absolute;left:66px;top:402px;width:330px;display:grid;grid-template-columns:1fr 1fr;row-gap:6px}
  .brew{padding:2px 8px 6px 10px;position:relative;height:72px}
  .brew:nth-child(odd){border-right:1px solid rgba(28,53,96,.45)}
  .brew:nth-child(n+3){border-top:1px solid rgba(28,53,96,.35);padding-top:7px;height:78px}
  .brew__title{font-weight:700;font-size:9px;letter-spacing:.3px;text-transform:uppercase;margin-bottom:3px}
  .brew__row{display:flex;align-items:center;gap:4px;font-size:6.5px;letter-spacing:.3px;text-transform:uppercase;line-height:11px}
  .brew__row svg{width:8px;height:8px;flex:none}
  .brew__pair{display:flex;gap:14px}
  .brew__gear{position:absolute;right:8px;bottom:8px;width:34px;height:38px;border-radius:4px;background:rgba(28,53,96,.14)}

  .storage{position:absolute;left:28px;right:28px;top:650px;text-align:center;font-size:7px;line-height:1.35}
  .storage__title{font-weight:700;font-size:7.5px}
  .contact{position:absolute;left:20px;right:20px;text-align:center;font-size:7px;line-height:1.4}
  .contact--address{top:692px}
  .contact--follow{top:706px}

  .front-claim{position:absolute;left:0;right:0;top:268px;text-align:center;color:var(--white);font-size:27px;font-weight:500;letter-spacing:.2px}
  .brand{position:absolute;left:0;right:0;top:528px;text-align:center}
  .brand__name{font-weight:600;font-size:66px;line-height:1;color:var(--gold);letter-spacing:1px}
  .brand__tag{margin-top:8px;font-weight:600;font-size:19px;color:var(--ink);letter-spacing:.2px}
  .label--front .side-note{top:510px}
</style>
</head>
<body>

<section class="label label--back" aria-label="Back label">
  <div class="label__pattern" role="img" aria-label="Navy line-art pattern of coffee leaves and cherries"></div>
  <p class="story"><strong>VELMIRA</strong> is a quality-driven coffee roaster focused on crafting fresh, flavorful coffee from <strong>premium beans sourced directly from farms.</strong> We build close relationships with growers to ensure ethical practices, traceability, and exceptional quality at the origin. Our small-batch roasting approach brings out the unique character of each bean—highlighting bold notes, rich complexity, and peak freshness. At <strong>VELMIRA</strong>, we believe great coffee starts at the source—and ends in your cup, roasted to perfection.</p>
  <div class="label__band"></div>
  <div class="seal" role="img" aria-label="Gold seal: whole bean, roasted by hand"></div>

  <div class="brew-guide">
    <div class="brew">
      <h3 class="brew__title">Drip Coffee</h3>
      <div class="brew__pair"><span class="brew__row"><svg viewBox="0 0 8 8"><circle cx="4" cy="4" r="3" fill="none" stroke="currentColor"/></svg>2 tbsp</span><span class="brew__row"><svg viewBox="0 0 8 8"><path d="M4 1 L6.5 5 A2.5 2.5 0 1 1 1.5 5 Z" fill="none" stroke="currentColor"/></svg>8 oz</span></div>
      <div class="brew__row"><svg viewBox="0 0 8 8"><rect x="1.5" y="1" width="5" height="6" fill="none" stroke="currentColor"/></svg>medium coarse</div>
      <div class="brew__row"><svg viewBox="0 0 8 8"><circle cx="4" cy="4" r="3" fill="none" stroke="currentColor"/><path d="M4 2v2h1.5" fill="none" stroke="currentColor"/></svg>3-4 min</div>
      <div class="brew__row"><svg viewBox="0 0 8 8"><rect x="1.5" y="2" width="4" height="5" fill="none" stroke="currentColor"/></svg>95-165 mg caffeine</div>
      <div class="brew__gear" role="img" aria-label="Drip coffee pot icon"></div>
    </div>
    <div class="brew">
      <h3 class="brew__title">Pour Over</h3>
      <div class="brew__pair"><span class="brew__row"><svg viewBox="0 0 8 8"><circle cx="4" cy="4" r="3" fill="none" stroke="currentColor"/></svg>2 tbsp</span><span class="brew__row"><svg viewBox="0 0 8 8"><path d="M4 1 L6.5 5 A2.5 2.5 0 1 1 1.5 5 Z" fill="none" stroke="currentColor"/></svg>8 oz</span></div>
      <div class="brew__row"><svg viewBox="0 0 8 8"><rect x="1.5" y="1" width="5" height="6" fill="none" stroke="currentColor"/></svg>medium</div>
      <div class="brew__row"><svg viewBox="0 0 8 8"><circle cx="4" cy="4" r="3" fill="none" stroke="currentColor"/><path d="M4 2v2h1.5" fill="none" stroke="currentColor"/></svg>3-4 min</div>
      <div class="brew__row"><svg viewBox="0 0 8 8"><rect x="1.5" y="2" width="4" height="5" fill="none" stroke="currentColor"/></svg>175 mg caffeine</div>
      <div class="brew__gear" role="img" aria-label="Pour over dripper icon"></div>
    </div>
    <div class="brew">
      <h3 class="brew__title">Glass Carafe</h3>
      <div class="brew__pair"><span class="brew__row"><svg viewBox="0 0 8 8"><circle cx="4" cy="4" r="3" fill="none" stroke="currentColor"/></svg>5 tbsp</span><span class="brew__row"><svg viewBox="0 0 8 8"><path d="M4 1 L6.5 5 A2.5 2.5 0 1 1 1.5 5 Z" fill="none" stroke="currentColor"/></svg>16 oz</span></div>
      <div class="brew__row"><svg viewBox="0 0 8 8"><rect x="1.5" y="1" width="5" height="6" fill="none" stroke="currentColor"/></svg>medium coarse</div>
      <div class="brew__row"><svg viewBox="0 0 8 8"><circle cx="4" cy="4" r="3" fill="none" stroke="currentColor"/><path d="M4 2v2h1.5" fill="none" stroke="currentColor"/></svg>4-5 min</div>
      <div class="brew__row"><svg viewBox="0 0 8 8"><rect x="1.5" y="2" width="4" height="5" fill="none" stroke="currentColor"/></svg>175 mg caffeine</div>
      <div class="brew__gear" role="img" aria-label="Glass carafe icon"></div>
    </div>
    <div class="brew">
      <h3 class="brew__title">French Press</h3>
      <div class="brew__pair"><span class="brew__row"><svg viewBox="0 0 8 8"><circle cx="4" cy="4" r="3" fill="none" stroke="currentColor"/></svg>6 tbsp</span><span class="brew__row"><svg viewBox="0 0 8 8"><path d="M4 1 L6.5 5 A2.5 2.5 0 1 1 1.5 5 Z" fill="none" stroke="currentColor"/></svg>18 oz</span></div>
      <div class="brew__row"><svg viewBox="0 0 8 8"><rect x="1.5" y="1" width="5" height="6" fill="none" stroke="currentColor"/></svg>coarse</div>
      <div class="brew__row"><svg viewBox="0 0 8 8"><circle cx="4" cy="4" r="3" fill="none" stroke="currentColor"/><path d="M4 2v2h1.5" fill="none" stroke="currentColor"/></svg>4 min</div>
      <div class="brew__row"><svg viewBox="0 0 8 8"><rect x="1.5" y="2" width="4" height="5" fill="none" stroke="currentColor"/></svg>80-107 mg caffeine</div>
      <div class="brew__gear" role="img" aria-label="French press icon"></div>
    </div>
    <div class="brew">
      <h3 class="brew__title">Espresso Machine</h3>
      <div class="brew__pair"><span class="brew__row"><svg viewBox="0 0 8 8"><circle cx="4" cy="4" r="3" fill="none" stroke="currentColor"/></svg>7 g</span><span class="brew__row"><svg viewBox="0 0 8 8"><path d="M4 1 L6.5 5 A2.5 2.5 0 1 1 1.5 5 Z" fill="none" stroke="currentColor"/></svg>14 g</span></div>
      <div class="brew__row"><svg viewBox="0 0 8 8"><rect x="1.5" y="1" width="5" height="6" fill="none" stroke="currentColor"/></svg>fine</div>
      <div class="brew__row"><svg viewBox="0 0 8 8"><circle cx="4" cy="4" r="3" fill="none" stroke="currentColor"/><path d="M4 2v2h1.5" fill="none" stroke="currentColor"/></svg>1 min</div>
      <div class="brew__row"><svg viewBox="0 0 8 8"><rect x="1.5" y="2" width="4" height="5" fill="none" stroke="currentColor"/></svg>67-75 mg caffeine</div>
      <div class="brew__gear" role="img" aria-label="Espresso machine icon"></div>
    </div>
    <div class="brew">
      <h3 class="brew__title">Cold Brew</h3>
      <div class="brew__pair"><span class="brew__row"><svg viewBox="0 0 8 8"><circle cx="4" cy="4" r="3" fill="none" stroke="currentColor"/></svg>10 tbsp</span><span class="brew__row"><svg viewBox="0 0 8 8"><path d="M4 1 L6.5 5 A2.5 2.5 0 1 1 1.5 5 Z" fill="none" stroke="currentColor"/></svg>16 oz</span></div>
      <div class="brew__row"><svg viewBox="0 0 8 8"><rect x="1.5" y="1" width="5" height="6" fill="none" stroke="currentColor"/></svg>extra coarse</div>
      <div class="brew__row"><svg viewBox="0 0 8 8"><circle cx="4" cy="4" r="3" fill="none" stroke="currentColor"/><path d="M4 2v2h1.5" fill="none" stroke="currentColor"/></svg>12-48 hr</div>
      <div class="brew__row"><svg viewBox="0 0 8 8"><rect x="1.5" y="2" width="4" height="5" fill="none" stroke="currentColor"/></svg>102-159 mg caffeine</div>
      <div class="brew__gear" role="img" aria-label="Iced cold brew glass icon"></div>
    </div>
  </div>

  <div class="side-note">ORGANIC &amp; FREETRADE</div>

  <div class="storage">
    <p class="storage__title">STORAGE:</p>
    <p>Proper storage is essential to maintaining your coffee’s freshness and flavor. Once opened, we recommend keeping your coffee in a cool, dark, dry place and sealed in an airtight container. Always reseal the bag after each use to preserve maximum freshness and aroma.</p>
  </div>
  <p class="contact contact--address">482 Fenwick Oakland Ca 94613</p>
  <p class="contact contact--follow">Follow Us:<br>www.velmira.com · TikTok@velmira · IG@tryvelmira</p>
</section>

<section class="label label--front" aria-label="Front label">
  <div class="label__pattern" role="img" aria-label="Navy line-art pattern of coffee leaves and cherries"></div>
  <p class="front-claim">100% ARABICA COFFEE BEANS</p>
  <div class="label__band"></div>
  <div class="seal" role="img" aria-label="Gold seal: whole bean, roasted by hand"></div>

  <div class="brand">
    <h1 class="brand__name">VELMIRA</h1>
    <p class="brand__tag">ETHICALLY SOURCED COFFEE BEANS</p>
  </div>

  <div class="side-note">ORGANIC &amp; FREETRADE</div>
</section>

</body>
</html>
```